Accounting business needs a great flyer

I need a flyer for my new business "Bright Ledger". I am an individual accountant working for himself on the Sunshine Coast in Queensland Australia. I would like to see designs that communicate reliability and trust. I believe my point of difference is that I am always available to my clients and I will cap my number of clients to ensure I can service them properly.
The main point I want to convey is that most of the time junior employees with little to no experience or unqualified employees do the tax work for the clients and a senior accountant quickly checks the work at the end but never gets to really know the clients business. Accountants in general seem to have a bad reputation for not responding to clients in a timely fashion, whether by email or phone. This is where I intend to differentiate myself. . I have also included some logo's that should go on the flyer.

Target Market(s)

Every small business

Industry/Entity Type

Public Accounting

Requirements
Must have
• Web address: www.brightledger.com.au
Phone number: 0418 592 637
Attached logos
Reference to: "Do you know who is actually doing your tax?"
Other accounting firms - use junior unqualified staff
- outsource to cheap labour countries
- use tax consultants who sometimes have had only 2 weeks training.
At Bright Ledger, a highly qualified CPA with a Masters in Taxation does your work from start to finish.
**I don't need it to say exactly this but I want the theme of the flyer to have these points in it.
Nice to have
• Something different

```html
<!DOCTYPE html>
<html lang="en">
<head>
<meta charset="utf-8">
<title>Bright Ledger Flyer</title>
<link rel="stylesheet" href="https://fonts.googleapis.com/css2?family=Poppins:wght@400;600;700;800&display=swap">
<style>
  :root {
    --navy: #25307a;
    --navy-deep: #1c2563;
    --yellow: #f7b500;
    --white: #ffffff;
    --ink: #3a3a3a;
    --grey-text: #555555;
    --backdrop: #4a4341;
    --badge-blue: #0d5bab;
    --badge-cyan: #13b5ea;
    --badge-grey: #c9c9c9;
  }
  * { margin: 0; padding: 0; box-sizing: border-box; }
  html, body {
    width: 1200px; height: 2371px; overflow: hidden;
    background: var(--backdrop);
    font-family: "Poppins", sans-serif;
  }
  .flyer {
    position: absolute; left: 72px; top: 502px;
    width: 1056px; height: 1367px;
    background: var(--white); overflow: hidden;
    box-shadow: 0 10px 30px rgba(0,0,0,0.35);
  }
  .flyer-shapes { position: absolute; inset: 0; }
  .brand {
    position: absolute; right: 36px; top: 36px; width: 380px;
    display: flex; flex-direction: column; align-items: center;
  }
  .brand-mark {
    width: 136px; height: 136px; border-radius: 50%;
    border: 5px solid #222;
  }
  .brand-name {
    margin-top: 26px; font-weight: 400; font-size: 34px;
    letter-spacing: 9px; color: #222; white-space: nowrap;
  }
  .pitch {
    position: absolute; right: 36px; top: 580px; width: 520px;
    text-align: right; color: var(--navy);
  }
  .pitch-lead { font-weight: 800; font-size: 66px; line-height: 62px; }
  .pitch-name { font-weight: 800; font-size: 50px; line-height: 62px; letter-spacing: -1px; white-space: nowrap; }
  .pitch-body {
    margin-top: 4px; font-size: 33px; line-height: 34px;
    color: var(--grey-text); text-transform: uppercase; font-weight: 400;
  }
  .pitch-body strong { color: var(--yellow); font-weight: 700; }
  .question {
    position: absolute; left: 34px; top: 682px;
    color: var(--white); font-weight: 800; font-size: 50px; line-height: 49px;
  }
  .compare {
    position: absolute; left: 34px; top: 940px; color: var(--white);
  }
  .compare-title { color: var(--yellow); font-weight: 700; font-size: 27px; line-height: 34px; margin-bottom: 6px; }
  .compare-list { list-style: none; font-size: 22.5px; line-height: 29px; }
  .compare-list li { position: relative; padding-left: 36px; margin-bottom: 6px; }
  .compare-list svg { position: absolute; left: 0; top: 4px; }
  .online-badge {
    position: absolute; left: 467px; top: 786px;
    width: 250px; height: 250px; border-radius: 50%;
    background: var(--yellow); color: var(--white);
    display: flex; align-items: center; justify-content: center;
    text-align: center; font-weight: 800; font-size: 34px; line-height: 37px;
    padding-bottom: 20px;
  }
  .contact-card {
    position: absolute; left: 34px; top: 1164px;
    width: 560px; height: 164px; border-radius: 30px;
    background: var(--white); padding: 16px 24px;
  }
  .contact-phone {
    display: flex; align-items: center; gap: 8px;
    font-weight: 700; font-size: 40px; line-height: 42px; color: var(--ink);
  }
  .contact-web { font-size: 26px; line-height: 30px; color: var(--ink); }
  .contact-web strong { color: var(--yellow); font-weight: 700; }
  .badges { display: flex; align-items: center; gap: 14px; margin-top: 10px; }
  .badge-rect { width: 120px; height: 52px; background: var(--badge-blue); }
  .badge-round { width: 42px; height: 42px; border-radius: 50%; background: var(--badge-grey); }
  .badge-cyan { width: 38px; height: 38px; border-radius: 50%; background: var(--badge-cyan); }
</style>
</head>
<body>
<main class="flyer">
  <svg class="flyer-shapes" viewBox="0 0 1056 1367" width="1056" height="1367">
    <defs>
      <linearGradient id="meetingTones" x1="0" y1="0.2" x2="1" y2="0.5">
        <stop offset="0" stop-color="#d9dee5"/>
        <stop offset="0.22" stop-color="#4a4f5e"/>
        <stop offset="0.45" stop-color="#263057"/>
        <stop offset="0.65" stop-color="#8f96a6"/>
        <stop offset="0.82" stop-color="#e7eaee"/>
        <stop offset="1" stop-color="#f5f6f8"/>
      </linearGradient>
      <linearGradient id="teamTones" x1="0" y1="0" x2="1" y2="0">
        <stop offset="0" stop-color="#2a3150"/>
        <stop offset="0.3" stop-color="#c9b49b"/>
        <stop offset="0.55" stop-color="#2b3048"/>
        <stop offset="0.8" stop-color="#6b5342"/>
        <stop offset="1" stop-color="#262b40"/>
      </linearGradient>
    </defs>
    <rect class="meeting-photo" x="0" y="0" width="1056" height="760" fill="url(#meetingTones)" role="img" aria-label="Photo of two accountants in suits meeting at an office table"/>
    <polygon class="white-field" points="0,898 1056,450 1056,1367 0,1367" fill="var(--white)"/>
    <polygon class="accent-stripe" points="474,697 1056,450 1056,462 474,709" fill="var(--navy)"/>
    <path class="navy-panel-edge" d="M0,664 L248,560 Q300,538 340,578 L560,818" fill="none" stroke="var(--white)" stroke-width="14"/>
    <path class="navy-panel" d="M0,672 L248,568 Q298,546 336,586 L556,826 L700,930 L760,1367 L0,1367 Z" fill="var(--navy)"/>
    <path class="team-photo" d="M340,1367 C380,1200 470,1030 600,985 Q630,975 680,975 L1056,975 L1056,1367 Z" fill="url(#teamTones)" role="img" aria-label="Photo of two smiling colleagues looking at a tablet"/>
  </svg>

  <header class="brand">
    <div class="brand-mark"></div>
    <div class="brand-name">BRIGHT LEDGER</div>
  </header>

  <section class="pitch">
    <div class="pitch-lead">AT</div>
    <div class="pitch-name">BRIGHT LEDGER</div>
    <p class="pitch-body">A <strong>HIGHLY QUALIFIED</strong><br>CPA WITH A MASTERS<br>IN TAXATION DOES<br>YOUR WORK<br>FROM <strong>START</strong><br>TO <strong>FINISH.</strong></p>
  </section>

  <h1 class="question">DO YOU<br>KNOW WHO IS<br>ACTUALLY<br>DOING<br>YOUR TAX?</h1>

  <section class="compare">
    <h2 class="compare-title">Other Accounting Firms Use</h2>
    <ul class="compare-list">
      <li><svg width="24" height="20" viewBox="0 0 24 20"><path d="M2,10 L9,17 L22,3" fill="none" stroke="var(--yellow)" stroke-width="4" stroke-linecap="round" stroke-linejoin="round"/></svg>Junior Unqualified Staff</li>
      <li><svg width="24" height="20" viewBox="0 0 24 20"><path d="M2,10 L9,17 L22,3" fill="none" stroke="var(--yellow)" stroke-width="4" stroke-linecap="round" stroke-linejoin="round"/></svg>Outsource To Cheap Labour Countries</li>
      <li><svg width="24" height="20" viewBox="0 0 24 20"><path d="M2,10 L9,17 L22,3" fill="none" stroke="var(--yellow)" stroke-width="4" stroke-linecap="round" stroke-linejoin="round"/></svg>Use Tax Consultants Who Sometimes<br>Have Had Only 2 Weeks Training.</li>
    </ul>
  </section>

  <div class="online-badge">ONLINE<br>SERVICE<br>AVAILABLE</div>

  <section class="contact-card">
    <div class="contact-phone">
      <svg width="32" height="32" viewBox="0 0 24 24"><path d="M6.6 10.8a15.1 15.1 0 0 0 6.6 6.6l2.2-2.2a1 1 0 0 1 1-.25 11.4 11.4 0 0 0 3.6.57 1 1 0 0 1 1 1V20a1 1 0 0 1-1 1A17 17 0 0 1 3 4a1 1 0 0 1 1-1h3.5a1 1 0 0 1 1 1c0 1.25.2 2.45.57 3.57a1 1 0 0 1-.25 1z" fill="var(--yellow)"/></svg>
      0418 592 637
    </div>
    <div class="contact-web">www.<strong>brightledger</strong>.com.au</div>
    <div class="badges">
      <div class="badge-rect"></div>
      <div class="badge-round"></div>
      <div class="badge-cyan"></div>
    </div>
  </section>
</main>
</body>
</html>
```